Coffee label for coffee brand - Kiln Lantern coffee

We want someone to design a label for packaging of a coffee line. The design will then be printed on stickers.

It is called Kiln Lantern Coffee (logo enclosed) I want to incorporate a streetscape and the idea is that with every different coffee it will be a different colour (we have 6 varieties at the moment) with a black background. It needs to have a modern feel.

It needs to have a blank area towards the bottom for the type of coffee which we will print later on)

text to include

'Roasting exceptional coffee'

Target Market(s)

Coffee drinkers - modern feel

Font styles to use
Sans Serif

Colors
f78f20
9bcb3b
33a6d7
b768aa

Requirements
Must have
• the logo incorporated
• Space for coffee variety
• Quote' Roasting exceptional coffee'
Nice to have
• Streetscape theme incorporated - bright colour varieties (would love metallic) (on black background)

```html
<!DOCTYPE html>
<html lang="en">
<head>
<meta charset="utf-8">
<title>Kiln Lantern Coffee – Dark Roast Label</title>
<link rel="stylesheet" href="https://fonts.googleapis.com/css2?family=Amatic+SC:wght@400;700&family=Special+Elite&display=swap">
<style>
  :root {
    --bg: #0b0b0b;
    --ink: #f2f2f2;
    --frame: #3d5866;
    --street-light: #3f6c80;
    --street-dark: #16262e;
    --roast-blue: #33a6d7;
    --expiry-red: #d8423f;
  }
  * { margin: 0; padding: 0; box-sizing: border-box; }
  html, body { width: 1200px; height: 1000px; overflow: hidden; background: var(--bg); }
  .label {
    position: relative;
    width: 1200px;
    height: 1000px;
    background:
      repeating-linear-gradient(0deg, rgba(255,255,255,0.018) 0 1px, transparent 1px 4px),
      var(--bg);
    font-family: "Amatic SC", sans-serif;
    color: var(--ink);
  }
  .frame-corners { position: absolute; left: 0; top: 0; }
  .tagline {
    position: absolute;
    top: 108px;
    left: 0; width: 1170px;
    text-align: center;
    font-size: 40px;
    font-weight: 400;
    letter-spacing: 1px;
  }
  .tagline-rule {
    position: absolute;
    top: 158px;
    left: 445px;
    width: 282px;
    height: 2px;
    background: var(--ink);
  }
  .organic {
    position: absolute;
    top: 167px;
    left: 0; width: 1170px;
    text-align: center;
    font-size: 40px;
    letter-spacing: 1px;
  }
  .streetscape {
    position: absolute;
    left: 300px;
    top: 228px;
    width: 572px;
    height: 565px;
    background: radial-gradient(ellipse at 70% 45%, var(--street-light) 0%, #2a4a59 35%, var(--street-dark) 75%, transparent 100%);
    opacity: 0.85;
    clip-path: polygon(0 50%, 60% 0, 100% 5%, 100% 85%, 85% 100%, 15% 100%, 0 80%);
  }
  .brand-name {
    position: absolute;
    top: 395px;
    left: 0; width: 1170px;
    text-align: center;
    font-size: 92px;
    font-weight: 700;
    line-height: 0.95;
    color: var(--ink);
  }
  .roast-stamp {
    position: absolute;
    left: 440px;
    top: 650px;
    width: 300px;
    height: 100px;
    transform: rotate(-9deg);
  }
  .roast-stamp svg { position: absolute; inset: 0; }
  .roast-name {
    position: absolute;
    inset: 0;
    display: flex;
    align-items: center;
    justify-content: center;
    font-family: "Special Elite", monospace;
    font-size: 36px;
    color: var(--roast-blue);
    letter-spacing: 1px;
  }
  .bean-type {
    position: absolute;
    top: 803px;
    left: 0; width: 1170px;
    text-align: center;
    font-size: 46px;
  }
  .net-weight {
    position: absolute;
    top: 858px;
    left: 0; width: 1170px;
    text-align: center;
    font-size: 26px;
    font-weight: 700;
  }
  .expiry {
    position: absolute;
    top: 828px;
    left: 774px;
    font-size: 26px;
    color: var(--expiry-red);
    letter-spacing: 0.5px;
  }
</style>
</head>
<body>
  <main class="label">
    <svg class="frame-corners" width="1200" height="1000" aria-hidden="true">
      <g fill="none" stroke="var(--frame)" stroke-width="2">
        <polyline points="390,114 270,114 270,213"/>
        <polyline points="778,114 900,114 900,213"/>
        <polyline points="270,783 270,881 390,881"/>
        <polyline points="900,783 900,881 778,881"/>
      </g>
    </svg>

    <p class="tagline">Roasting exceptional coffee</p>
    <div class="tagline-rule"></div>
    <p class="organic">100% organic coffee</p>

    <div class="streetscape" role="img" aria-label="Sketched city street scene with a coffee shop front, trees and a skyline in muted blue"></div>

    <h1 class="brand-name">Kiln Lantern<br>Coffee</h1>

    <div class="roast-stamp">
      <svg width="300" height="100" aria-hidden="true">
        <g fill="none" stroke="var(--roast-blue)" stroke-width="2">
          <polyline points="14,40 8,40 8,70"/>
          <polyline points="8,82 8,92 22,92"/>
          <polyline points="272,8 292,8 292,22"/>
          <polyline points="292,40 292,62 285,62"/>
        </g>
      </svg>
      <span class="roast-name">DARK ROAST</span>
    </div>

    <p class="bean-type">Whole bean</p>
    <p class="net-weight">Net weight &nbsp;250 gram</p>
    <p class="expiry">EXP NOV 2018</p>
  </main>
</body>
</html>
```